Mirabo & Orvan Automotive Repair Shop. Need a new website design.

We specialize in Mirabo & Orvan auto repair, but also work on other Asian import vehicles. We have been in business for 7 years and pride ourselves on high quality auto repair that is fixed right the first time. Would like the automotive repair website to incorporate the colors black, red and white if possible and have our logo and some Mirabo and Orvan vehicles included in the website.

Target Market(s)

Mirabo & Orvan vehicle owners

Industry/Entity Type

Automotive Repair

Coding

Coded - Design and coding required

Number of Pages Required

5+ page

Colors
EB3D1F
EC4F4E
F09395
F8D3D4
FCEDEE

Requirements
Must have
• Home, Services, Contact Us, Schedule appointment, and a gallery tab that I can add shop pictures to when completed.
Nice to have
• Would like to see example pictures of job next to each service listed.
Should not have
• Service not related to auto repair. Ex. auto detailing, towing, car wash

```html
<!DOCTYPE html>
<html lang="en">
<head>
<meta charset="utf-8">
<title>Vantor Automotive</title>
<link rel="stylesheet" href="https://fonts.googleapis.com/css2?family=Oswald:wght@400;500;600;700&family=Poppins:wght@400;500;600&display=swap">
<style>
:root{
  --red:#e3201f;
  --red-soft:#ec4f4e;
  --black:#0a0a0a;
  --ink:#141414;
  --panel:#3a3a3a;
  --band:#2c2c2c;
  --white:#ffffff;
  --muted:#cfcfcf;
  --line:#5a5a5a;
}
*{margin:0;padding:0;box-sizing:border-box}
html,body{width:1200px;height:3948px;overflow:hidden}
body{position:relative;background:var(--black);color:var(--white);font-family:"Poppins",sans-serif}
.abs{position:absolute}
.display{font-family:"Oswald",sans-serif;text-transform:uppercase}
.red{color:var(--red)}

/* header + hero */
.hero{left:0;top:0;width:1200px;height:662px;background:
  radial-gradient(ellipse 420px 260px at 22% 70%,#4a4c50 0%,transparent 70%),
  radial-gradient(ellipse 380px 240px at 82% 60%,#55575c 0%,transparent 70%),
  radial-gradient(ellipse at 55% 30%,#3c3d41 0%,#1c1c1e 55%,#0b0b0c 90%)}
.hero-shade{left:0;top:0;width:1200px;height:662px;background:linear-gradient(180deg,rgba(0,0,0,.45) 0%,rgba(0,0,0,.1) 40%,rgba(0,0,0,.55) 100%)}
.brand{display:flex;align-items:center;gap:10px;font-family:"Oswald",sans-serif;font-weight:700;font-size:26px;letter-spacing:1px;color:var(--white)}
.brand-mark{width:30px;height:30px;background:var(--red)}
.nav{left:470px;top:61px;display:flex;gap:26px;font-family:"Oswald",sans-serif;font-size:13px;text-transform:uppercase;letter-spacing:.5px}
.btn{background:var(--red);color:var(--white);font-family:"Oswald",sans-serif;text-transform:uppercase;font-size:13px;letter-spacing:.5px;display:flex;align-items:center;justify-content:center}
.hero-kicker{left:0;width:1200px;top:290px;text-align:center;font-family:"Oswald",sans-serif;font-size:22px;color:var(--red);text-transform:uppercase}
.hero-title{left:0;width:1200px;top:322px;text-align:center;font-family:"Oswald",sans-serif;font-weight:600;font-size:58px;line-height:66px;text-transform:uppercase}
.scroll{left:0;width:1200px;top:545px;text-align:center;font-family:"Oswald",sans-serif;font-size:13px;text-transform:uppercase}

/* service tiles */
.tiles{left:0;top:662px;width:1200px;height:268px;display:flex}
.tile{flex:1;position:relative;border-right:2px solid var(--black)}
.tile:nth-child(1){background:radial-gradient(ellipse at 40% 40%,#8c8c8c,#444 50%,#161616)}
.tile:nth-child(2){background:radial-gradient(ellipse at 60% 35%,#7a6a5a,#333 50%,#121212)}
.tile:nth-child(3){background:radial-gradient(ellipse at 50% 30%,#b9b9b9,#5a5a5a 50%,#1a1a1a)}
.tile:nth-child(4){background:radial-gradient(ellipse at 45% 40%,#d23232,#6a1a1a 50%,#1a1a1a)}
.tile::after{content:"";position:absolute;inset:0;background:linear-gradient(180deg,transparent 45%,rgba(0,0,0,.6))}
.tile-label{position:absolute;left:26px;top:180px;font-family:"Oswald",sans-serif;font-size:21px;text-transform:uppercase;z-index:1}

/* welcome */
.eyebrow{font-family:"Oswald",sans-serif;font-size:13px;color:var(--red);text-transform:uppercase}
.section-title{font-family:"Oswald",sans-serif;font-size:28px;text-transform:uppercase}
.body-copy{font-size:14px;line-height:24px;color:var(--white)}
.portrait{left:725px;top:1088px;width:195px;height:370px;background:linear-gradient(180deg,#6b6f74,#4a3c3c 45%,#8d1c1c 75%,#3a3a3a)}
.intro{left:240px;top:1620px;width:720px;text-align:center;font-size:14px;line-height:24px}

/* values */
.glow{left:0;top:1760px;width:1200px;height:460px;background:radial-gradient(ellipse at 50% 15%,#b3161a 0%,#5a0c0e 35%,var(--black) 75%)}
.value{width:338px;height:300px;background:var(--panel);text-align:center;padding:0 40px;display:flex;flex-direction:column;align-items:center;justify-content:center}
.value h3{font-family:"Oswald",sans-serif;font-weight:500;font-size:21px;text-transform:uppercase;margin:18px 0 10px}
.value p{font-size:14px;line-height:23px}

/* testimonial */
.testi-photo{left:135px;top:2240px;width:390px;height:360px;border:4px solid var(--red);border-radius:46px 120px 46px 46px;background:linear-gradient(150deg,#8d9196,#55585c 45%,#a11d1d 85%)}
.stars{color:var(--red);font-size:18px;letter-spacing:2px}

/* makes */
.makes{left:0;top:2668px;width:1200px;height:256px;background:var(--band)}
.make-row{left:100px;top:2795px;width:1000px;display:flex;gap:10px}
.make{flex:1;height:66px;background:var(--white);color:#1a1a1a;display:flex;align-items:center;justify-content:center;font-family:"Oswald",sans-serif;font-size:17px;text-transform:uppercase;letter-spacing:1px}

/* contact */
.car{left:0;top:2930px;width:610px;height:600px;background:radial-gradient(ellipse at 30% 55%,#c99a3c 0%,#6b4a1a 35%,#120d06 75%)}
.field{font-size:12px;border-bottom:1px solid var(--line);padding-bottom:12px}

/* footer */
.footer{left:0;top:3540px;width:1200px;height:408px;background:var(--ink);border-top:4px solid var(--red)}
.f-label{font-family:"Oswald",sans-serif;font-size:12px;text-transform:uppercase;color:var(--white)}
.f-text{font-size:12px;line-height:18px;color:var(--muted);margin-bottom:10px}
.f-links{font-size:13px;line-height:24px}
.social{display:flex;gap:14px;font-size:12px}
.social span{display:flex;align-items:center;gap:5px}
.social i{width:10px;height:10px;border-radius:50%;background:var(--white);display:inline-block}
</style>
</head>
<body>

<!-- Hero -->
<section class="abs hero" role="img" aria-label="Mechanic working in an engine bay, dark workshop background"></section>
<div class="abs hero-shade"></div>
<div class="abs brand" style="left:100px;top:32px"><span class="brand-mark"></span>VANTOR</div>
<nav class="abs nav"><span>Home</span><span>Services</span><span>About us</span><span>Gallery</span><span>Directions</span><span>Contact us</span></nav>
<div class="abs btn" style="left:928px;top:52px;width:176px;height:32px">Schedule an appointment</div>

<svg class="abs" style="left:582px;top:222px" width="36" height="36" viewBox="0 0 36 36"><circle cx="18" cy="18" r="16" fill="none" stroke="#fff" stroke-width="2"/><path d="M14 11 L26 18 L14 25 Z" fill="#fff"/></svg>
<div class="abs hero-kicker">Serving the Mirabo, Orvan, &amp; Asian auto community</div>
<h1 class="abs hero-title">Dealership quality at<br>affordable prices"</h1>
<div class="abs scroll">Scroll down &#8250;</div>

<!-- Service tiles -->
<div class="abs tiles">
  <div class="tile" role="img" aria-label="Timing belt components"><span class="tile-label">Timing belts</span></div>
  <div class="tile" role="img" aria-label="Engine tune-up"><span class="tile-label">Tune-ups</span></div>
  <div class="tile" role="img" aria-label="Open hood of a car"><span class="tile-label">Front engine seals</span></div>
  <div class="tile" role="img" aria-label="Red car in the shop"><span class="tile-label">More services</span></div>
</div>

<!-- Welcome -->
<div class="abs eyebrow" style="left:100px;top:1004px">Your Mirabo &amp; Orvan specialist</div>
<h2 class="abs section-title" style="left:100px;top:1030px">Welcome to <span class="red">Vantor Automotive</span></h2>
<p class="abs body-copy" style="left:100px;top:1092px;width:560px">Vantor Automotive, your reliable shop for all auto repair needs. We specialize in Mirabo &amp; Orvan vehicles and also repair all other asian import vehicles. We focus on achieving the highest quality in our work to ensure you're back on the road quickly.</p>
<div class="abs" style="left:100px;top:1350px;display:flex;align-items:center;gap:14px">
  <span class="display" style="font-size:12px">Contact us today</span>
  <span class="btn" style="width:150px;height:38px;border-radius:20px;gap:8px;font-size:14px"><svg width="14" height="14" viewBox="0 0 24 24"><path d="M6.6 10.8a15 15 0 006.6 6.6l2.2-2.2a1 1 0 011-.25 11.4 11.4 0 003.6.6 1 1 0 011 1V20a1 1 0 01-1 1A17 17 0 013 4a1 1 0 011-1h3.5a1 1 0 011 1c0 1.25.2 2.45.6 3.6a1 1 0 01-.25 1z" fill="#fff"/></svg>555-014-2270</span>
</div>
<div class="abs" style="left:708px;top:1072px;width:60px;height:60px;border-left:6px solid var(--red);border-top:6px solid var(--red)"></div>
<div class="abs portrait" role="img" aria-label="Smiling mechanic in a red and grey uniform"></div>

<p class="abs intro">Receive top notch, honest, reliable service from our team with over 20 years experience in Mirabo &amp; Orvan dealerships. Owner is an Guild Certified Master Technician who has experience managing an entire team of technicians in big name dealerships, assisting them in their diagnosis &amp; repair work. What does this mean for you, our loyal customer? It means you are entrusting your vehicle to highly trained specialists who have both the knowledge &amp; skill to provide you with service excellence comparable to none.</p>

<!-- Values -->
<div class="abs glow"></div>
<div class="abs value" style="left:100px;top:1848px">
  <svg width="46" height="46" viewBox="0 0 46 46"><circle cx="23" cy="23" r="20" fill="none" stroke="#e3201f" stroke-width="4"/><path d="M28 16c-1.5-1.5-8-2.5-8 1.5s9 2.5 9 7-7 4-9 2M23 11v24" fill="none" stroke="#e3201f" stroke-width="3"/></svg>
  <h3>Save money</h3>
  <p>We provide reasonable labor rates equal to about half of big name dealership labor rates!</p>
</div>
<div class="abs value" style="left:431px;top:1848px">
  <svg width="46" height="46" viewBox="0 0 46 46"><path d="M15 28 L10 44 L18 40 L23 44 L23 30 Z M31 28 L36 44 L28 40 L23 44 L23 30 Z" fill="#e3201f"/><circle cx="23" cy="17" r="14" fill="#e3201f"/><path d="M23 9l2.4 5 5.4.6-4 3.7 1.1 5.3-4.9-2.7-4.9 2.7 1.1-5.3-4-3.7 5.4-.6z" fill="#3a3a3a"/></svg>
  <h3>Only the best</h3>
  <p>Genuine Mirabo &amp; Orvan and original manufacturer parts are used at our facility to assure longevity of repairs.</p>
</div>
<div class="abs value" style="left:762px;top:1848px">
  <svg width="46" height="46" viewBox="0 0 46 46"><path d="M23 3 L40 9 V22 C40 33 32 40 23 43 C14 40 6 33 6 22 V9 Z" fill="#e3201f"/><path d="M15 23 L21 29 L32 17" fill="none" stroke="#3a3a3a" stroke-width="4"/></svg>
  <h3>We stand behind our work</h3>
  <p>We offer a 12k mile / 12months warranty.</p>
</div>

<!-- Testimonial -->
<div class="abs testi-photo" role="img" aria-label="Happy customer seated in a car"></div>
<div class="abs" style="left:575px;top:2240px;width:560px;height:380px;background:radial-gradient(ellipse at 65% 60%,#5a0c0e 0%,#2a0607 40%,transparent 72%)" role="img" aria-label="Faint red car silhouette"></div>
<h2 class="abs section-title" style="left:575px;top:2270px;font-size:24px">Testimonials</h2>
<div class="abs stars" style="left:575px;top:2340px">&#9733;&#9733;&#9733;&#9733;&#9733;</div>
<p class="abs body-copy" style="left:575px;top:2368px;width:420px">I would highly recommend Vantor Automotive to family, friends, &amp; co-workers! I'm a repeat customer myself!</p>
<p class="abs body-copy" style="left:575px;top:2440px">Daniel R</p>
<div class="abs" style="left:586px;top:2500px;display:flex;gap:8px"><i style="width:8px;height:8px;border-radius:50%;background:#fff"></i><i style="width:8px;height:8px;border-radius:50%;background:#777"></i></div>

<!-- Makes -->
<section class="abs makes"></section>
<h2 class="abs section-title" style="left:0;width:1200px;top:2732px;text-align:center;font-size:24px">We also repair other import makes such as</h2>
<div class="abs make-row">
  <div class="make">Haruko</div><div class="make">Avelo</div><div class="make">Kiro</div><div class="make">Hanseo</div><div class="make">Nomura</div><div class="make"></div><div class="make">Infera</div>
</div>

<!-- Contact -->
<div class="abs car" role="img" aria-label="Headlight of a gold car at night"></div>
<div class="abs display" style="left:690px;top:2998px;font-size:12px">Contact us</div>
<h2 class="abs display" style="left:690px;top:3020px;font-size:42px;line-height:48px;font-weight:500">Have questions?<br>Get in touch!</h2>
<div class="abs field" style="left:690px;top:3148px;width:210px">Name</div>
<div class="abs field" style="left:920px;top:3148px;width:200px">Last Name</div>
<div class="abs field" style="left:690px;top:3200px;width:210px">Email</div>
<div class="abs field" style="left:920px;top:3200px;width:200px">Phone</div>
<div class="abs field" style="left:690px;top:3252px;width:430px;height:80px">Message</div>
<div class="abs btn" style="left:690px;top:3400px;width:140px;height:38px;gap:6px">&#10148; Get in touch</div>

<!-- Footer -->
<footer class="abs footer"></footer>
<div class="abs brand" style="left:100px;top:3640px"><span class="brand-mark"></span>VANTOR</div>
<div class="abs" style="left:380px;top:3628px;width:300px">
  <div class="f-label">Office</div><div class="f-text">(555) 014-2270 / 555-018-3391</div>
  <div class="f-label">Email</div><div class="f-text">hello@vantorauto.example</div>
  <div class="f-label">Location</div><div class="f-text">42 Harbor Works Lane #3 Fairview, TX 75000</div>
  <div class="f-label">Hours of operation</div><div class="f-text">Monday - Friday, 8:30 AM - 6:00 PM</div>
</div>
<div class="abs" style="left:750px;top:3628px">
  <div class="f-label red">Links</div>
  <div class="f-links">Home<br>Services<br>About us<br>Gallery<br>Directions<br>Contact us</div>
</div>
<div class="abs" style="left:920px;top:3628px">
  <div class="f-label red" style="margin-bottom:10px">Follow us on</div>
  <div class="social"><span><i></i>Facio</span><span><i></i>Snapra</span><span><i></i>Linko</span><span><i></i>Tika</span></div>
</div>
<div class="abs" style="left:100px;top:3906px;font-size:11px;color:var(--muted)">Vantor Automotive &copy; 2024. All rights reserved.</div>

</body>
</html>
```